Business Cards

The name of our firm is "Bayfield Insurance adjusters"
We separate ourselves from all other public adjusters because most of us worked for the insurance companies so we understand their games.
As Insurance adjusters we represent the Insured, not the insurance companies. Our # 1 priority is to handle the entire claim process as seamless as possible on behalf of the homeowner/business owner so they don't have to deal with the hassles and headaches. Just as the logo your team designed, I want the cards to stand out from everyone elses. I also want the cards to help better understand our services and Value on hiring us and value that we can offer.
I uploaded the logo whenever I created the project. I don't see an option on re uploading the logo anywhere. Any advise??

```html
<!DOCTYPE html>
<html lang="en">
<head>
<meta charset="utf-8">
<title>Bayfield Insurance Adjusters – Business Cards</title>
<link rel="stylesheet" href="https://fonts.googleapis.com/css2?family=Poppins:wght@400;500;700;800&display=swap">
<style>
  :root {
    --backdrop: #1d1f22;
    --card-white: #ffffff;
    --brand-blue: #0a5c97;
    --brand-blue-light: #0a7db8;
    --brand-blue-deep: #064a7e;
    --ink: #1e2226;
    --divider: #2b6aa3;
  }
  * { box-sizing: border-box; margin: 0; padding: 0; }
  html, body {
    width: 1200px; height: 900px; overflow: hidden;
    background: var(--backdrop);
    font-family: "Poppins", sans-serif;
  }
  .sheet {
    width: 1200px; height: 900px;
    display: flex; flex-direction: column; align-items: center; justify-content: center;
    gap: 40px;
  }
  .card {
    width: 700px; height: 400px;
    border-radius: 4px;
    box-shadow: 0 14px 40px rgba(0,0,0,.55);
    position: relative; overflow: hidden;
  }
  /* front */
  .card--front {
    background: var(--card-white);
    display: flex; align-items: center;
  }
  .card__brand {
    width: 330px; padding-left: 60px;
    color: var(--brand-blue);
    font-weight: 800; text-transform: uppercase;
    line-height: 1.05;
  }
  .card__brand-name { display: block; font-size: 46px; letter-spacing: 1px; }
  .card__brand-sub { display: block; font-size: 13.5px; letter-spacing: 2.4px; margin-top: 6px; }
  .card__divider {
    width: 1.5px; height: 230px;
    background: var(--divider);
    margin: 0 40px 0 20px;
  }
  .card__details { color: var(--ink); }
  .card__person {
    color: var(--brand-blue);
    font-weight: 700; font-size: 25px; text-transform: uppercase; letter-spacing: 1px;
  }
  .card__role {
    color: var(--brand-blue);
    font-weight: 500; font-size: 16px; text-transform: uppercase; letter-spacing: 1px;
    margin-bottom: 14px;
  }
  .contact { display: flex; align-items: center; gap: 10px; font-size: 16px; margin-top: 6px; }
  .contact svg { width: 16px; height: 16px; flex: none; }
  /* back */
  .card--back {
    background: linear-gradient(180deg, var(--brand-blue-light) 0%, var(--brand-blue) 55%, var(--brand-blue-deep) 100%);
    display: flex; align-items: center; justify-content: center;
  }
  .card__brand--reverse {
    width: auto; padding: 0; text-align: center;
    color: var(--card-white);
  }
  .card__brand--reverse .card__brand-name { font-size: 58px; }
  .card__brand--reverse .card__brand-sub { font-size: 16px; letter-spacing: 3px; }
</style>
</head>
<body>
<main class="sheet">
  <section class="card card--front" aria-label="Business card front">
    <div class="card__brand">
      <span class="card__brand-name">Bayfield</span>
      <span class="card__brand-sub">Insurance adjusters</span>
    </div>
    <div class="card__divider"></div>
    <div class="card__details">
      <p class="card__person">Daniel Reyes</p>
      <p class="card__role">Managing Director</p>
      <p class="contact">
        <svg viewBox="0 0 24 24" aria-hidden="true"><path fill="var(--brand-blue)" d="M6.6 10.8a15.1 15.1 0 0 0 6.6 6.6l2.2-2.2c.3-.3.7-.4 1-.2 1.1.4 2.3.6 3.6.6.6 0 1 .4 1 1V20c0 .6-.4 1-1 1A17 17 0 0 1 3 4c0-.6.4-1 1-1h3.5c.6 0 1 .4 1 1 0 1.3.2 2.5.6 3.6.1.3 0 .7-.2 1z"/></svg>
        555-014-2273
      </p>
      <p class="contact">
        <svg viewBox="0 0 24 24" aria-hidden="true"><rect x="2" y="5" width="20" height="14" rx="1.5" fill="var(--brand-blue)"/><path d="M3 6l9 7 9-7" fill="none" stroke="#fff" stroke-width="1.6"/></svg>
        daniel@bayfieldadj.com
      </p>
    </div>
  </section>

  <section class="card card--back" aria-label="Business card back">
    <div class="card__brand card__brand--reverse">
      <span class="card__brand-name">Bayfield</span>
      <span class="card__brand-sub">Insurance adjusters</span>
    </div>
  </section>
</main>
</body>
</html>
```